BrevoLunt Business Card Design Project

We are looking for a modern, clean business card design for our new company. We are a consulting firm focused on the financial services market providing management and IT consulting to banks, insurance companies, etc. Please include our company logo and company contact information from the attached file in the design. Two versions of the logo are attached, either version is acceptable. Logos are available in other file formats if needed. We would like to include the contact information for both our UK and US offices as well as the following information for each individual card holder: Name, position/title, address, phone number and e-mail address.
Updates
Project Deadline Extended
Reason: A last minute trip over seas has prevented us from finalizing the decision. A decision will be made this week. We apologize for the inconvenience.
Industry/Entity Type
Business
Contact Information for Business Card
Company logo.
Company locations and phone numbers for both the US and UK offices.
Company URL.
Cardholder Name
Cardholder Position/title
Cardholder Address
Cardholder Phone Number
Cardholder e-mail Address
Look and feel
Each slider illustrates characteristics of the customer's brand and the style your logo design should communicate.

```html
<!DOCTYPE html>
<html lang="en">
<head>
<meta charset="utf-8">
<title>BrevoLunt Partners – Business Card</title>
<link rel="stylesheet" href="https://fonts.googleapis.com/css2?family=Open+Sans:wght@400;600;700&display=swap">
<style>
  :root {
    --backdrop: #e8e6e3;
    --card-white: #ffffff;
    --navy: #13305a;
    --slate: #5f6062;
    --text-grey: #444648;
    --rule-grey: #8a8a8a;
    --muted-light: #b9bec7;
    --white: #ffffff;
  }
  * { box-sizing: border-box; margin: 0; padding: 0; }
  html, body {
    width: 1200px; height: 1000px; overflow: hidden;
    background: var(--backdrop);
    font-family: "Open Sans", Arial, sans-serif;
  }
  .canvas { position: relative; width: 1200px; height: 1000px; }

  .card {
    position: absolute; left: 265px; width: 666px; height: 397px;
    overflow: hidden; box-shadow: 0 4px 14px rgba(0,0,0,.18);
  }
  .card--front { top: 73px; background: var(--card-white); }
  .card--back { top: 533px; background: var(--navy); color: var(--white); }

  /* Front */
  .brand { position: absolute; display: flex; align-items: center; gap: 12px; }
  .brand__mark { width: 26px; height: 26px; background: var(--navy); }
  .brand__name { font-weight: 700; font-size: 34px; color: var(--navy); letter-spacing: -0.3px; white-space: nowrap; }
  .card--front .brand { left: 32px; top: 150px; }

  .holder { position: absolute; right: 32px; top: 210px; text-align: right; }
  .holder__name { font-size: 22px; font-weight: 600; color: var(--navy); line-height: 1; }
  .holder__title { font-size: 15px; color: var(--text-grey); margin-top: 12px; }
  .holder-tab { position: absolute; right: 0; top: 214px; width: 10px; height: 40px; background: var(--navy); }
  .divider { position: absolute; left: 32px; top: 246px; width: 480px; height: 1px; background: var(--rule-grey); }
  .divider--short { left: 512px; width: 122px; }

  .contacts { position: absolute; left: 32px; top: 276px; list-style: none; }
  .contacts li { display: flex; align-items: center; gap: 8px; font-size: 16.5px; color: var(--text-grey); height: 26px; }
  .contacts svg { width: 15px; height: 15px; fill: var(--navy); flex: none; }

  .bands { position: absolute; left: 0; bottom: 0; width: 666px; height: 32px; }

  /* Back */
  .office { position: absolute; left: 33px; font-size: 16.5px; line-height: 20px; }
  .office--us { top: 58px; }
  .office--uk { top: 222px; }
  .office__country { font-weight: 700; font-size: 17.5px; margin-bottom: 8px; }
  .office__phone { display: flex; align-items: center; gap: 6px; margin-top: 4px; }
  .office__phone svg { width: 15px; height: 13px; fill: var(--white); }

  .card--back .brand { left: 350px; top: 205px; width: 285px; justify-content: center; }
  .card--back .brand__name { color: var(--white); font-size: 32px; }
  .card--back .brand__mark { background: var(--white); width: 22px; height: 22px; }
  .web { position: absolute; left: 346px; top: 303px; width: 292px; text-align: center;
         font-size: 15px; letter-spacing: 2.6px; color: var(--muted-light); }
</style>
</head>
<body>
<main class="canvas">

  <section class="card card--front" aria-label="Business card front">
    <div class="brand">
      <span class="brand__mark"></span>
      <span class="brand__name">BrevoLunt Partners</span>
    </div>

    <div class="holder-tab"></div>
    <div class="holder">
      <p class="holder__name">Dana R. Whitlow</p>
      <p class="holder__title">Office Manager</p>
    </div>
    <div class="divider"></div>
    <div class="divider divider--short"></div>

    <ul class="contacts">
      <li><svg viewBox="0 0 16 16"><rect x="4" y="0" width="8" height="16" rx="1.5"/><rect x="5.5" y="2" width="5" height="6" fill="#fff"/></svg>+ 000 000 0000</li>
      <li><svg viewBox="0 0 16 16"><path d="M1 3h14v10H1z"/><path d="M1 3l7 6 7-6" fill="none" stroke="#fff" stroke-width="1.3"/></svg>info@brevoluntpartners.com</li>
      <li><svg viewBox="0 0 16 16"><circle cx="8" cy="8" r="7"/><path d="M1 8h14M8 1c-3 3-3 11 0 14M8 1c3 3 3 11 0 14" fill="none" stroke="#fff" stroke-width="1"/></svg>www.brevoluntpartners.com</li>
    </ul>

    <svg class="bands" viewBox="0 0 666 32" preserveAspectRatio="none" aria-hidden="true">
      <polygon points="0,0 318,0 302,32 0,32" fill="var(--slate)"/>
      <polygon points="326,0 666,0 666,32 310,32" fill="var(--navy)"/>
    </svg>
  </section>

  <section class="card card--back" aria-label="Business card back">
    <div class="office office--us">
      <p class="office__country">United States</p>
      <p>482 N Harlow Ave,</p>
      <p>Suite 210-214</p>
      <p>Maplewood UT 84120</p>
      <p class="office__phone"><svg viewBox="0 0 16 14"><path d="M1 5c0-3 14-3 14 0v1h-4V4H5v2H1z"/><path d="M3 7h10l1 6H2z"/></svg>(801) 555-0147</p>
    </div>

    <div class="office office--uk">
      <p class="office__country">Great Britain</p>
      <p>14-16 Calder Street</p>
      <p>London</p>
      <p>N4 2PL</p>
      <p class="office__phone"><svg viewBox="0 0 16 14"><path d="M1 5c0-3 14-3 14 0v1h-4V4H5v2H1z"/><path d="M3 7h10l1 6H2z"/></svg>+44 7700 900412</p>
    </div>

    <div class="brand">
      <span class="brand__mark"></span>
      <span class="brand__name">BrevoLunt Partners</span>
    </div>
    <p class="web">www.brevoluntpartners.com</p>
  </section>

</main>
</body>
</html>
```